Marlowe Holdings LLC - Business Cards

Need the following information on the cards:

Name: Dean R Vossler
Title: Chief Executive Manager

Business address:
412 N Ridgeview Lane #118
Larkfield Springs, Il 60412

Phone: (555) 555-0148 - Business
KPV FFL license number: 5-21-xxx-xx-xx-04519
Email: dean.vossler@marloweholdingsffl.com

Target Market(s)

Firearm owners

Industry/Entity Type

Firearms industry,

Contact Information for Business Card

Contact number, name and title, web page address, email, business address and kpv license number,

Requirements
Must have
• Name, title, business address, phone numbers, KPV license numbers, web page address and email address.
Nice to have
• Cellphone number,

```html
<!DOCTYPE html>
<html lang="en">
<head>
<meta charset="utf-8">
<title>Marlowe Holdings LLC – Business Cards</title>
<link rel="stylesheet" href="https://fonts.googleapis.com/css2?family=Open+Sans:wght@400;600&family=Montserrat:wght@700&display=swap">
<style>
  :root {
    --stage: #2b2b2b;
    --card-red: #cc1b22;
    --card-red-deep: #b3151c;
    --card-white: #ffffff;
    --ink-dark: #1a1a1a;
    --text-light: #ffffff;
  }
  * { margin: 0; padding: 0; box-sizing: border-box; }
  html, body { width: 1200px; height: 1015px; overflow: hidden; }
  body {
    background: var(--stage);
    font-family: "Open Sans", sans-serif;
    display: flex;
    align-items: center;
    justify-content: center;
    gap: 40px;
  }
  .card {
    position: relative;
    width: 540px;
    height: 309px;
    background: var(--card-red);
    overflow: hidden;
    box-shadow: 0 14px 30px rgba(0,0,0,.5);
  }
  /* back of card */
  .card-back .brand-mark {
    position: absolute;
    left: 50%;
    top: 42%;
    transform: translate(-50%, -50%);
    display: flex;
    align-items: center;
    gap: 12px;
  }
  .card-back .brand-mark .badge {
    width: 30px; height: 30px;
    border-radius: 50%;
    background: var(--card-red-deep);
  }
  .card-back .brand-mark .brand-name {
    font-weight: 600;
    font-size: 26px;
    color: var(--card-red-deep);
    white-space: nowrap;
  }
  .card-back .license {
    position: absolute;
    left: 0; right: 0;
    bottom: 58px;
    text-align: center;
    color: var(--text-light);
    font-size: 15px;
  }
  /* front of card */
  .card-front .white-panel {
    position: absolute;
    inset: 0;
  }
  .card-front .brand-mark {
    position: absolute;
    left: 348px;
    top: 120px;
    width: 180px;
    text-align: center;
  }
  .card-front .brand-name {
    font-weight: 600;
    font-size: 22px;
    line-height: 1.2;
    color: var(--card-red);
  }
  .card-front .identity {
    position: absolute;
    left: 30px;
    top: 54px;
    color: var(--text-light);
    font-family: "Montserrat", sans-serif;
    font-weight: 700;
    text-transform: uppercase;
  }
  .identity .person-name { font-size: 19px; letter-spacing: .5px; }
  .identity .person-title { font-size: 10.5px; letter-spacing: .6px; margin-top: 2px; }
  .card-front .address {
    position: absolute;
    left: 58px;
    top: 140px;
    color: var(--text-light);
    font-size: 13px;
    line-height: 1.35;
  }
  .card-front .contact-list {
    position: absolute;
    left: 58px;
    top: 206px;
    list-style: none;
    color: var(--text-light);
    font-size: 12px;
    line-height: 1.5;
  }
  .contact-list li { display: flex; align-items: center; gap: 6px; white-space: nowrap; }
  .contact-list svg { width: 12px; height: 12px; flex: none; }
</style>
</head>
<body>

  <section class="card card-back" aria-label="Card back">
    <div class="brand-mark">
      <span class="badge"></span>
      <span class="brand-name">Marlowe Holdings LLC</span>
    </div>
    <p class="license">KPV FFL License No: 5-21-xxx-xx-xx-04519</p>
  </section>

  <section class="card card-front" aria-label="Card front">
    <svg class="white-panel" viewBox="0 0 540 309" preserveAspectRatio="none" aria-hidden="true">
      <path d="M540 0 L330 0 C 275 60 290 240 380 262 C 440 275 500 262 540 245 Z" fill="var(--card-white)"/>
      <path d="M345 30 C 300 90 305 225 385 250 C 430 262 470 258 500 250" fill="none" stroke="var(--ink-dark)" stroke-width="3"/>
    </svg>

    <div class="brand-mark">
      <p class="brand-name">Marlowe Holdings LLC</p>
    </div>

    <div class="identity">
      <p class="person-name">Dean R Vossler</p>
      <p class="person-title">Chief Executive Manager</p>
    </div>

    <p class="address">412 N Ridgeview Lane #118<br>Larkfield Springs, Il 60412</p>

    <ul class="contact-list">
      <li>
        <svg viewBox="0 0 24 24" fill="var(--text-light)"><path d="M6.6 10.8a15 15 0 0 0 6.6 6.6l2.2-2.2c.3-.3.7-.4 1-.2 1.1.4 2.3.6 3.6.6.6 0 1 .4 1 1V20c0 .6-.4 1-1 1A17 17 0 0 1 3 4c0-.6.4-1 1-1h3.5c.6 0 1 .4 1 1 0 1.3.2 2.5.6 3.6.1.3 0 .7-.2 1z"/></svg>
        (555) 555-0148
      </li>
      <li>
        <svg viewBox="0 0 24 24" fill="none" stroke="var(--text-light)" stroke-width="2"><rect x="6" y="2" width="12" height="20" rx="2"/><line x1="11" y1="18" x2="13" y2="18"/></svg>
        (555) 555-0148
      </li>
      <li>
        <svg viewBox="0 0 24 24" fill="var(--text-light)"><path d="M2 5h20v14H2z M2 5l10 8 10-8" stroke="var(--card-red)" stroke-width="1.5"/></svg>
        dean.vossler@marloweholdingsffl.com
      </li>
      <li>
        <svg viewBox="0 0 24 24" fill="none" stroke="var(--text-light)" stroke-width="2"><circle cx="12" cy="12" r="10"/><path d="M2 12h20M12 2c3 3 3 17 0 20M12 2c-3 3-3 17 0 20"/></svg>
        www.marloweholdingsffl.com
      </li>
    </ul>
  </section>

</body>
</html>
```